Re-design of current business cards

We are updating our website with new colors and layout. Would like to re-design our business cards to co-ordinate. See attached pdf with new Brindlecraft website colors. We would also like to combine our 2 brands on the one business card. Attached is the new design for our Brindlecraft website, current business cards, which are one sided, brindlecraft logo in tiff, .ai for fonts. Brindlecraft logo font is Optimum, Quillmarsh website home page image, Quillmarsh brand statics for products which includes the logo for this brand.

Quillmarsh brand will stay the dark gray on the website. See attached statics for product and website home page.
Updates

The business cards will be 2 sided. Brindlecraft Brand on one side and Quillmarsh Brand on the other. The colors for Brindlecraft need to follow the color scheme of the brindlecraft website pdf I uploaded. The colors are a blue, lighter teal blue and white. Quillmarsh needs to follow the dark gray color on files uploaded

Target Market(s)

The trade and consumers

Industry/Entity Type

Home Furnishing

Contact Information for Business Card

We are updating our website with new colors and layout. Would like to re-design our business cards to co-ordinate. We would also like to combine our 2 brands onto 1 2 sided business cards.

Requirements
Must have
• Colors that match our new website, see attached image.
• RGB colors
• navy -#152842
• teal - 98aeb9
• The gray color used for Quillmarsh brands.
• ll logos and fonts should stay the same.

```html
<!DOCTYPE html>
<html lang="en">
<head>
<meta charset="utf-8">
<title>Brindlecraft and Quillmarsh Business Card</title>
<link href="https://fonts.googleapis.com/css2?family=Marcellus&family=Lato:wght@400;700&display=swap" rel="stylesheet">
<style>
  :root {
    --page-bg: #e4e4e4;
    --navy: #152842;
    --teal: #98aeb9;
    --card-gray: #5b5b5d;
    --white: #ffffff;
    --soft-white: #e9e9e9;
    --photo-dark: #4a4644;
    --photo-mid: #8a847d;
    --photo-light: #b7b2ab;
  }
  * { margin: 0; padding: 0; box-sizing: border-box; }
  html, body { width: 1200px; height: 800px; overflow: hidden; }
  body {
    background: var(--page-bg);
    font-family: "Lato", sans-serif;
    color: var(--white);
    position: relative;
  }
  .card {
    position: absolute;
    box-shadow: 0 6px 18px rgba(0,0,0,0.18);
    overflow: hidden;
  }
  .card::before, .card::after {
    content: "";
    position: absolute;
    background: var(--edge-line, var(--white));
  }
  .card::before { left: 10px; top: 0; bottom: 10px; width: 4px; }
  .card::after { left: 10px; right: 0; bottom: 10px; height: 4px; }

  .brand-name {
    font-family: "Marcellus", serif;
    letter-spacing: 1px; text-transform: uppercase;
    color: var(--white); line-height: 1; white-space: nowrap;
  }

  /* Brindlecraft side */
  .card-brindlecraft {
    left: 60px; top: 240px; width: 560px; height: 320px;
    background: var(--navy);
    --edge-line: var(--teal);
  }
  .front-brand {
    position: absolute; left: 0; right: 0; top: 112px;
    display: flex; align-items: center; justify-content: center; gap: 14px;
  }
  .card-brindlecraft .brand-name { font-size: 48px; }
  .brand-dot {
    width: 32px; height: 32px; border-radius: 50%;
    background: var(--teal); flex: none;
  }
  .front-url {
    position: absolute; left: 0; right: 0; top: 178px;
    text-align: center; font-family: "Marcellus", serif;
    font-size: 14px; color: var(--teal); letter-spacing: 0.5px;
  }

  /* Quillmarsh side */
  .card-quillmarsh {
    left: 760px; top: 120px; width: 320px; height: 560px;
    background: var(--card-gray);
  }
  .back-brand {
    position: absolute; left: 20px; right: 0; top: 42px; text-align: center;
  }
  .card-quillmarsh .brand-name { font-size: 34px; }
  .back-url {
    display: block; margin-top: 8px;
    font-family: "Marcellus", serif; font-size: 10px; color: var(--soft-white);
  }
  .photo-rule {
    position: absolute; left: 58px; right: 36px; height: 5px;
    background: var(--white); border-radius: 3px;
  }
  .photo-rule.top { top: 108px; }
  .photo-rule.bottom { top: 330px; }
  .photo-area {
    position: absolute; left: 66px; right: 44px; top: 118px; height: 206px;
    background: linear-gradient(160deg, var(--photo-light) 0%, var(--photo-mid) 45%, var(--photo-dark) 100%);
  }
  .contact {
    position: absolute; left: 58px; right: 30px; top: 356px;
    font-size: 11px; line-height: 1.5; color: var(--soft-white);
  }
  .contact-name {
    font-weight: 700; font-size: 15px; letter-spacing: 4px;
    text-transform: uppercase; color: var(--white);
  }
  .contact-title { margin-bottom: 12px; }
  .contact-rule { height: 1px; background: var(--soft-white); margin: 5px 0; }
  .label { font-weight: 700; color: var(--white); }
</style>
</head>
<body>
  <section class="card card-brindlecraft">
    <div class="front-brand">
      <span class="brand-name">Brindlecraft</span>
      <span class="brand-dot"></span>
    </div>
    <div class="front-url">www.brindlecraft.com</div>
  </section>

  <section class="card card-quillmarsh">
    <div class="back-brand">
      <div class="brand-name">Quillmarsh</div>
      <span class="back-url">www.quillmarsh.com</span>
    </div>
    <div class="photo-rule top"></div>
    <div class="photo-area" role="img" aria-label="Interior photograph of framed wall art, a mirror and furniture in a gray room"></div>
    <div class="photo-rule bottom"></div>
    <div class="contact">
      <div class="contact-name">Dana Whitlock</div>
      <div class="contact-title">Graphics/Photography Director</div>
      <div>PO BOX 214/1870 Cedar Bend Rd</div>
      <div>Millbrook, Ohio 43012</div>
      <div class="contact-rule"></div>
      <div><span class="label">P</span> 555.210.4387 | <span class="label">F</span> 555.210.4392</div>
      <div class="contact-rule"></div>
      <div><span class="label">EMAIL</span> dwhitlock@brindlecraft.com</div>
    </div>
  </section>
</body>
</html>
```